Tree company needs modern website design

We need a website design for a tree company, here are some websites they like:

http://korvalemarine.com/company/ - we like the big image filling most of the page. Also the top half of the page looks good with the logo along top and good task bar also (we don’t like the spiel on left hand side covering up the picture + too many words!) If we could have our logo at lop like this along with our slogan which is 'Healthy Trees Grown for Lasting Shade'

http://www.pinecroftgardens.co.nz/ - we like the bottom half of this with the clean lines and welcome to part down bottom rather than the spiel to the left as on above site. Also like the moving leaves, any chance we could have birds such as a fantail, Tui and Bellbirds flying across the page and also some birdsong playing?

This is their existing website, that needs an updated design: http://tallfernwood.co.nz/

Industry/Entity Type

It Company

Font styles to use
Serif
Sans Serif

Requirements
Must have
• "Website by Pages Built Simple" located in bottom right hand side
Use images provided as background or banner images
Should not have
• Social Media icons

```html
<!DOCTYPE html>
<html lang="en">
<head>
<meta charset="utf-8">
<title>Tall Fernwood Trees</title>
<link rel="stylesheet" href="https://fonts.googleapis.com/css2?family=Oxygen:wght@300;400;700&display=swap">
<style>
:root{
  --cream:#fcfbe2;
  --teal:#0b5e5c;
  --teal-deep:#0a5452;
  --ink:#1c1c1c;
  --body:#555;
  --rule:#d6d6d6;
  --gold:#f4d51a;
  --white:#fff;
}
*{margin:0;padding:0;box-sizing:border-box}
html,body{width:910px;height:1200px;overflow:hidden;background:var(--white)}
body{font-family:'Oxygen',Arial,sans-serif;color:var(--ink);position:relative}
.site-header{position:absolute;left:0;top:0;width:910px;height:106px;background:var(--cream)}
.brand{position:absolute;left:76px;top:30px;display:flex;align-items:center;gap:7px}
.brand-dot{width:13px;height:13px;border-radius:50%;background:var(--teal)}
.brand-name{font-size:20px;font-weight:700;color:var(--teal);letter-spacing:.3px;white-space:nowrap}
.slogan{position:absolute;left:90px;top:70px;font-size:12px;color:var(--teal);white-space:nowrap}
.main-nav{position:absolute;top:51px;left:0;width:910px;font-size:11.5px}
.main-nav a{position:absolute;color:var(--ink);text-decoration:none;white-space:nowrap}
.main-nav a.current{color:var(--teal);font-weight:700}
.hero{position:absolute;left:0;top:106px;width:910px;height:446px;
  background:linear-gradient(180deg,#cfe0ee 0%,#e9eff3 25%,#5f7a45 45%,#4a6a35 62%,#9a9478 80%,#a6a49a 100%)}
.hero-caption{position:absolute;left:66px;top:148px;width:358px;height:130px;border-radius:8px;
  background:rgba(11,94,92,.88);padding:20px 22px;color:var(--white)}
.hero-caption .kicker{font-size:19px;line-height:24px}
.hero-caption .headline{font-size:24px;line-height:30px}
.hero-caption p{font-size:10px;line-height:16px;font-weight:300;margin-top:6px;opacity:.9}
.hero-dots{position:absolute;left:431px;top:428px;display:flex;gap:4px}
.hero-dots span{width:9px;height:9px;border-radius:50%;background:#111}
.welcome{position:absolute;left:76px;top:582px;width:758px}
.welcome h1{font-size:21px;font-weight:400;padding-bottom:10px;border-bottom:1px solid var(--rule)}
.welcome p{font-size:10px;line-height:16px;color:var(--body);margin-top:13px}
.audio-player{position:absolute;left:77px;top:742px}
.projects{position:absolute;left:76px;top:796px;width:758px}
.projects h2{font-size:19px;font-weight:400;color:var(--teal)}
.project{position:absolute;width:380px;height:82px}
.project .thumb{position:absolute;left:0;top:0;width:114px;height:82px}
.project .text{position:absolute;left:125px;top:2px;width:240px}
.project h3{font-size:11.5px;font-weight:700;color:#444}
.project p{font-size:10px;line-height:15px;color:var(--body);margin-top:4px}
.project a{display:block;margin-top:3px;font-size:11.5px;font-weight:700;color:var(--teal);text-decoration:none}
.site-footer{position:absolute;left:0;top:1094px;width:910px;height:106px;background:var(--teal)}
.footer-links{position:absolute;left:77px;top:30px;font-size:11.5px;color:var(--white)}
.footer-links a{color:var(--white);text-decoration:none}
.footer-links .sep{margin:0 6px}
.copyright{position:absolute;left:77px;top:56px;font-size:9.5px;color:#d9ecea}
.footer-brand{position:absolute;right:80px;top:28px;display:flex;align-items:center;gap:6px}
.footer-brand .brand-dot{background:var(--gold);width:11px;height:11px}
.footer-brand .brand-name{font-size:16px;color:var(--gold)}
.credit{position:absolute;right:82px;top:70px;font-size:9.5px;color:#cfe4e2}
</style>
</head>
<body>
<header class="site-header">
  <div class="brand"><span class="brand-dot"></span><span class="brand-name">TALL FERNWOOD TREES</span></div>
  <div class="slogan">Healthy Trees Grown for Lasting Shade</div>
  <nav class="main-nav">
    <a class="current" style="left:354px" href="#">HOME</a>
    <a style="left:423px" href="#">ABOUT US</a>
    <a style="left:505px" href="#">TREE GALLERY</a>
    <a style="left:609px" href="#">PROJECTS</a>
    <a style="left:687px" href="#">CATALOGUE</a>
    <a style="left:779px" href="#">CONTACT</a>
  </nav>
</header>

<section class="hero" role="img" aria-label="Photo of a tree-lined residential road with tall conifers under a cloudy sky">
  <div class="hero-caption">
    <div class="kicker">Pellentesque faucibus accumsan</div>
    <div class="headline">Cras ante vitae enim iaculis</div>
    <p>Aliquam nec erat at purus cursus interdum Vestibulum ligula augue bibendum accumsan vestibulum ut commodo Morbi</p>
  </div>
  <div class="hero-dots"><span></span><span></span><span></span><span></span></div>
</section>

<section class="welcome">
  <h1>Welcome to Tall Fernwood Trees Mainpage</h1>
  <p>Etiam eu urna Sed porta Suspendisse quam leo molestie sed luctus quis feugiat in pede Fusce tellus Sed metus augue convallis et vehicula ut pulvinar eu ante Integer orci tellus tristique vitae consequat nec porta vel lectus Nulla sit amet diam Duis non nunc libero a tempus libero lectus feugiat felis</p>
  <p>Etiam eu urna Sed porta Suspendisse quam leo molestie sed luctus quis feugiat in pede Fusce tellus Sed metus augue convallis et vehicula ut pulvinar eu ante Integer orci tellus tristique vitae consequat nec porta vel lectus Nulla sit amet diam Duis non nunc libero a tempus libero lectus feugiat felis Morbi diam mauris viverra in gravida eu mattis in ante Morbi eget arcu Morbi porta libero id ullamcorper nonummy nibh ligula pulvinar metus eget consv</p>
</section>

<svg class="audio-player" width="186" height="19" viewBox="0 0 186 19" aria-label="Audio player">
  <rect x="0" y="0" width="186" height="19" rx="3" fill="#2a2a2a"/>
  <path d="M10 4.5 L10 14.5 L19 9.5 Z" fill="#fff"/>
  <rect x="30" y="8" width="64" height="3" rx="1.5" fill="#666"/>
  <circle cx="37" cy="9.5" r="4.5" fill="#eee"/>
  <text x="102" y="13" font-family="Oxygen,sans-serif" font-size="8" font-weight="700" fill="#fff">0:22</text>
  <path d="M130 7 L133 7 L137 4 L137 15 L133 12 L130 12 Z" fill="#fff"/>
  <path d="M139.5 6.5 Q142 9.5 139.5 12.5" stroke="#fff" stroke-width="1.2" fill="none"/>
  <rect x="149" y="8" width="26" height="3" rx="1.5" fill="#ccc"/>
  <circle cx="174" cy="9.5" r="4" fill="#fff"/>
</svg>

<section class="projects">
  <h2>Latest Projects</h2>
  <article class="project" style="left:0;top:37px">
    <div class="thumb" role="img" aria-label="Photo of a house below snowy mountains" style="background:linear-gradient(180deg,#5a86c4 0%,#9a9a95 45%,#4d5a3a 100%)"></div>
    <div class="text"><h3>Consequat nec porta vel</h3><p>lectus Nulla sit amet diam Duis non nunc libero a tempus libero lectus feugiat felis Morbi diam mauris viverra in gravida eu mattis in ante</p><a href="#">Read More</a></div>
  </article>
  <article class="project" style="left:386px;top:37px">
    <div class="thumb" role="img" aria-label="Photo of a modern building with landscaping" style="background:linear-gradient(180deg,#3e78c9 0%,#b9c2c8 50%,#7c8378 100%)"></div>
    <div class="text"><h3>Consequat nec porta vel</h3><p>lectus Nulla sit amet diam Duis non nunc libero a tempus libero lectus feugiat felis Morbi diam mauris viverra in gravida eu mattis in ante</p><a href="#">Read More</a></div>
  </article>
  <article class="project" style="left:386px;top:151px">
    <div class="thumb" role="img" aria-label="Photo of young trees beside a gravel path" style="background:linear-gradient(180deg,#3b6cb8 0%,#d9dde2 45%,#6d7a4c 75%,#8f8a80 100%)"></div>
    <div class="text"><h3>Consequat nec porta vel</h3><p>lectus Nulla sit amet diam Duis non nunc libero a tempus libero lectus feugiat felis Morbi diam mauris viverra in gravida eu mattis in ante</p><a href="#">Read More</a></div>
  </article>
  <article class="project" style="left:0;top:151px">
    <div class="thumb" role="img" aria-label="Photo of a timber house entrance with plantings" style="background:linear-gradient(180deg,#6b5a45 0%,#4a6fa8 50%,#5d6b4a 100%)"></div>
    <div class="text"><h3>Consequat nec porta vel</h3><p>lectus Nulla sit amet diam Duis non nunc libero a tempus libero lectus feugiat felis Morbi diam mauris viverra in gravida eu mattis in ante</p><a href="#">Read More</a></div>
  </article>
</section>

<footer class="site-footer">
  <nav class="footer-links">
    <a href="#">About Us</a><span class="sep">|</span><a href="#">Blog</a><span class="sep">|</span><a href="#">Catalogue</a><span class="sep">|</span><a href="#">Contact</a><span class="sep">|</span><a href="#">Product Galleries</a><span class="sep">|</span><a href="#">Projects</a>
  </nav>
  <div class="copyright">© 2013 Tall Fernwood Trees. All right reserved</div>
  <div class="footer-brand"><span class="brand-dot"></span><span class="brand-name">TALL FERNWOOD TREES</span></div>
  <div class="credit">Website by Pages Built Simple</div>
</footer>
</body>
</html>
```